Visitenkarten-Design für Goldankauf und Verkauf von Trauringen
Zielgruppe
Goldankauf und Verkauf von Trauringen
Aufgabenstellung
Edel, nicht zu bunt, das Design soll sich dem Kunden einprägen, ansprechend, gerne können auch Wasserzeichen verwendet werden.

```html
<!DOCTYPE html>
<html lang="de">
<head>
<meta charset="utf-8">
<title>Aurelia Ringhaus – Visitenkarte</title>
<link rel="stylesheet" href="https://fonts.googleapis.com/css2?family=Roboto:wght@300;400;700&display=swap">
<style>
  :root {
    --stage: #231f20;
    --card-dark: #0a0a0a;
    --card-glow: #3b3b3b;
    --card-white: #ffffff;
    --gold: #d6ad3c;
    --gold-light: #f3cf55;
    --gold-deep: #b07f2a;
    --contact-text: #f6e2a6;
    --ink: #111111;
    --silver: #cfcfcf;
  }
  * { margin: 0; padding: 0; box-sizing: border-box; }
  html, body {
    width: 1200px; height: 1199px; overflow: hidden;
    background: var(--stage);
    font-family: "Roboto", Arial, sans-serif;
  }
  .canvas { position: relative; width: 1200px; height: 1199px; }

  .card-front {
    position: absolute; left: 231px; top: 51px; width: 831px; height: 471px;
    background: radial-gradient(ellipse at 48% 30%, var(--card-glow) 0%, #1a1a1a 45%, var(--card-dark) 100%);
  }
  .brand-front {
    position: absolute; left: 0; right: 0; top: 150px; text-align: center;
  }
  .brand-front .brand-name {
    display: block; font-weight: 300; font-size: 70px; letter-spacing: 1px;
    color: var(--gold);
  }
  .brand-front .brand-rule {
    display: block; width: 500px; height: 2px; margin: 6px auto 8px;
    background: var(--gold-deep);
  }
  .brand-front .brand-tagline {
    display: block; font-weight: 300; font-size: 26px; color: var(--silver);
  }

  .card-back {
    position: absolute; left: 240px; top: 656px; width: 831px; height: 465px;
    background: var(--card-white); overflow: hidden;
  }
  .card-back svg.back-shapes { position: absolute; inset: 0; }

  .person { position: absolute; left: 0; width: 372px; text-align: center; color: var(--ink); }
  .person-name { top: 170px; font-size: 37px; font-weight: 300; letter-spacing: 0.5px; }
  .person-name strong { font-weight: 700; }
  .person-role { top: 222px; font-size: 19px; font-weight: 400; }

  .brand-back { position: absolute; left: 18px; top: 350px; }
  .brand-back .brand-name {
    display: block; font-weight: 300; font-size: 34px; color: var(--gold-deep);
  }
  .brand-back .brand-tagline {
    display: block; margin-top: 4px; font-weight: 300; font-size: 14px; color: #9a9a9a;
  }

  .contact {
    position: absolute; font-size: 19px; font-weight: 400; line-height: 30px;
    color: var(--contact-text); letter-spacing: 0.2px; white-space: nowrap;
  }
  .contact-address { left: 466px; top: 104px; }
  .contact-web { left: 476px; top: 194px; }
  .contact-mail { left: 471px; top: 274px; }
  .contact-phone { left: 454px; top: 354px; }
</style>
</head>
<body>
<main class="canvas">

  <section class="card-front" aria-label="Vorderseite">
    <div class="brand-front">
      <span class="brand-name">Aurelia Ringhaus</span>
      <span class="brand-rule"></span>
      <span class="brand-tagline">Goldankauf &amp; Trauringe</span>
    </div>
  </section>

  <section class="card-back" aria-label="Rückseite">
    <svg class="back-shapes" width="831" height="465" viewBox="0 0 831 465">
      <defs>
        <linearGradient id="gold-band" x1="0" y1="0" x2="1" y2="0">
          <stop offset="0" stop-color="var(--gold-deep)"/>
          <stop offset="0.35" stop-color="var(--gold-light)"/>
          <stop offset="0.7" stop-color="var(--gold)"/>
          <stop offset="1" stop-color="var(--gold-deep)"/>
        </linearGradient>
        <radialGradient id="dark-panel" cx="0.4" cy="0.5" r="0.7">
          <stop offset="0" stop-color="#333333"/>
          <stop offset="0.55" stop-color="#141414"/>
          <stop offset="1" stop-color="#000000"/>
        </radialGradient>
      </defs>
      <path class="dark-panel" d="M400,0 Q508,232 400,465 L831,465 L831,0 Z" fill="url(#dark-panel)"/>
      <path class="gold-band" d="M320,0 Q430,232 320,465 L404,465 Q510,232 404,0 Z" fill="url(#gold-band)"/>
      <g class="contact-icons" fill="var(--ink)">
        <path d="M401,122 a9,9 0 0 1 9,9 c0,7 -9,16 -9,16 c0,0 -9,-9 -9,-16 a9,9 0 0 1 9,-9 Z M401,127 a4,4 0 1 0 0.01,0 Z" fill-rule="evenodd"/>
        <g fill="none" stroke="var(--ink)" stroke-width="3" stroke-linecap="round">
          <rect x="390" y="208" width="13" height="8" rx="4" transform="rotate(-45 396 212)"/>
          <rect x="399" y="199" width="13" height="8" rx="4" transform="rotate(-45 405 203)"/>
        </g>
        <rect x="391" y="281" width="20" height="14" rx="1.5"/>
        <path d="M392,282 L401,290 L410,282" fill="none" stroke="#e4b94a" stroke-width="1.6"/>
        <path d="M394,357 c2,-2 4,-2 5,0 l2,4 c1,2 0,3 -1,4 c1,3 4,6 7,7 c1,-1 2,-2 4,-1 l4,2 c2,1 2,3 0,5 c-2,2 -5,3 -8,2 c-7,-3 -12,-8 -15,-15 c-1,-3 0,-6 2,-8 Z"/>
      </g>
    </svg>

    <div class="person person-name">JOHN <strong>SMITH</strong></div>
    <div class="person person-role">CREATIVE DIRECTOR</div>

    <div class="brand-back">
      <span class="brand-name">Aurelia Ringhaus</span>
      <span class="brand-tagline">Goldankauf &amp; Trauringe</span>
    </div>

    <div class="contact contact-address">FIRST ADDRESS LINE<br>SECOND ADDRESS LINE</div>
    <div class="contact contact-web">WWW.YOURCOMPANY.COM</div>
    <div class="contact contact-mail">J.SMITH@YOURCOMPANY.COM</div>
    <div class="contact contact-phone">+0 123 456 789 324</div>
  </section>

</main>
</body>
</html>
```